TILVERA.COM is a premium domain sales company. Our competitors are companies like brankoport.com, selvatrix.com, quimbelstock.com. Our current site is at www.tilveras.com.

We want to have the ability to search for domains, to highlight special offers and have some testimonials on the index page.

The logo for the site is attached.

Please be sure that the order form fits on the screen without scrolling the page. I want the entire form, including the submit button to fit without any page scrolling.

Delivered product - INDEX PAGE, ORDER FORM AND CONTENT PAGE PSDs.

Target Market(s)

Small to Medium business professionals

Industry/Entity Type

It Company

Requirements
Must have
• 1. List of domains for sale
2. Simple search box with button to run the search
3. link for advanced search
4. testimonial area. Note - this can be a small box where a different testimonial is displayed on each page load.
Nice to have
• Would like the site to have some white space. Don't want a heavily packed website. Give it an "airy" feel.

```html
<!DOCTYPE html>
<html lang="en">
<head>
<meta charset="utf-8">
<title>TILVERA.COM – Premium Domains</title>
<link href="https://fonts.googleapis.com/css2?family=PT+Sans:wght@400;700&family=Roboto:wght@400;500;700&display=swap" rel="stylesheet">
<style>
:root{
  --page:#efefec;
  --panel:#fbfbfa;
  --blue:#0a5aa8;
  --blue-bright:#2b7fd0;
  --navy:#0b3f86;
  --green:#2f8f1f;
  --green-dark:#0f7a36;
  --text:#333;
  --muted:#777;
  --red:#d8271f;
  --orange:#d9821a;
  --footer:#2f2f2f;
  --footer-bar:#232323;
  --footer-text:#a9a9a9;
}
*{box-sizing:border-box;margin:0;padding:0}
html,body{width:946px;height:1200px;overflow:hidden}
body{background:var(--page);font-family:"PT Sans",Arial,sans-serif;color:var(--text);position:relative}
.sheet{position:absolute;left:98px;top:0;width:751px;height:1200px;background:var(--panel);box-shadow:0 0 3px rgba(0,0,0,.12)}
.abs{position:absolute}
.brand{left:22px;top:40px;display:flex;align-items:center;gap:8px;font-family:"Roboto",sans-serif;font-weight:700;font-size:26px;color:var(--green)}
.brand-dot{width:18px;height:18px;border-radius:50%;background:var(--green)}
.support{left:552px;top:44px;display:flex;align-items:center;gap:8px}
.support small{display:block;font-size:11px;color:var(--navy)}
.support strong{display:block;font-family:"Roboto",sans-serif;font-weight:400;font-size:19px;color:#222;letter-spacing:.5px}
.nav{left:0;top:102px;width:751px;height:36px;background:var(--blue);display:flex;align-items:center}
.nav a{position:absolute;color:#fff;font-size:12.5px;font-weight:700;text-decoration:none}
.search{left:552px;top:6px;width:184px;height:24px;background:#fff;border:2px solid #d9e86a;border-radius:2px;font-size:11.5px;color:#aaa;padding:2px 9px}
.search svg{position:absolute;right:8px;top:5px}
.hero{left:16px;top:150px;width:719px;height:258px;background:#fff;box-shadow:0 1px 3px rgba(0,0,0,.2)}
.hero-photo{left:0;top:0;width:432px;height:258px;background:linear-gradient(135deg,#a99c8c 0%,#d7cfc4 45%,#efece6 100%)}
.register{left:433px;top:22px;width:271px;height:214px;background:#f3f3f3;border:1px solid #e0e0e0}
.register h1{position:absolute;left:17px;top:18px;font-family:"Roboto",sans-serif;font-weight:700;font-size:22px;color:var(--navy);letter-spacing:-.3px}
.domain-input{left:0;top:58px;width:265px;height:30px;background:#fff;border:1px solid #ddd;font-size:11px;color:#999;padding:8px 32px}
.domain-input i{position:absolute;left:17px;top:12px;width:7px;height:7px;border:1.5px solid #2b9bd0;border-radius:50%}
.register p{position:absolute;left:13px;top:98px;width:240px;font-size:12.5px;color:#666;line-height:16px}
.cta{left:12px;top:142px;width:140px;height:35px;background:linear-gradient(#3ba72b,#228b17);border-radius:2px;color:#fff;font-family:"Roboto",sans-serif;font-weight:500;font-size:15px;padding:8px 12px}
.cta svg{position:absolute;right:12px;top:8px}
.adv{left:16px;top:190px;font-size:11.5px;color:var(--blue);text-decoration:underline;padding-left:18px}
.adv svg{position:absolute;left:0;top:1px}
.dir-title{left:33px;top:422px;font-family:"Roboto",sans-serif;font-size:18px;color:#333}
.directory{left:11px;top:456px;width:724px;border-collapse:collapse;font-size:11.5px}
.directory th{background:var(--green-dark);color:#fff;font-weight:700;text-align:left;height:32px;padding-left:24px;font-size:12px}
.directory td{height:28.6px;padding-left:24px;border-left:1px solid #e4e4e4;color:#333}
.directory td:first-child{border-left:none}
.directory tr:nth-child(odd) td{background:#f6f6f6}
.directory tr:nth-child(even) td{background:#fff}
.buy{color:var(--blue)}
.sold{color:var(--red)}
.why{left:15px;top:774px;width:720px;height:44px;background:var(--blue-bright);color:#fff;font-family:"Roboto",sans-serif;font-size:17.5px}
.why span{position:absolute;top:12px}
.why i{position:absolute;left:30px;top:44px;border:12px solid transparent;border-top:8px solid var(--blue-bright)}
.feature h3{position:absolute;font-family:"Roboto",sans-serif;font-weight:400;font-size:17px;white-space:nowrap}
.feature p{position:absolute;font-size:10px;color:#777;line-height:15px;width:190px}
.quote{width:190px;font-size:9.5px;line-height:15px;color:#666}
.quote b{display:block;color:var(--green-dark);font-size:10.5px;margin-top:3px}
.footer{left:0;top:1008px;width:751px;height:160px;background:var(--footer)}
.footer h4{position:absolute;top:22px;font-family:"Roboto",sans-serif;font-weight:400;font-size:16.5px;color:#eee}
.footer ul{position:absolute;top:52px;list-style:none;font-size:9.5px;letter-spacing:.8px;color:var(--footer-text);line-height:15.2px}
.map{left:508px;top:49px;width:209px;height:93px;border:2px solid #ccc;background:linear-gradient(135deg,#e6e2d2,#d9d3bb)}
.bottom{left:0;top:1168px;width:751px;height:32px;background:var(--footer-bar);font-size:10px;color:#ddd;padding:10px 20px}
.bottom span{position:absolute;right:36px;top:10px}
</style>
</head>
<body>
<div class="sheet">
  <div class="abs brand"><span class="brand-dot"></span>TILVERA.COM</div>
  <div class="abs support">
    <svg width="34" height="34" viewBox="0 0 34 34" aria-hidden="true"><path d="M6 20a11 11 0 0 1 22 0" fill="none" stroke="#333" stroke-width="3"/><rect x="3" y="18" width="7" height="11" rx="2" fill="#333"/><rect x="24" y="18" width="7" height="11" rx="2" fill="#333"/><path d="M27 29q0 4-8 4" fill="none" stroke="#333" stroke-width="1.5"/></svg>
    <div><small>24/7 Online Support Service</small><strong>1-800-412-5530</strong></div>
  </div>

  <nav class="abs nav">
    <a style="left:22px">Home</a>
    <a style="left:93px">Deleting domains</a>
    <a style="left:228px">Domains for sale</a>
    <a style="left:359px">Testimonials</a>
    <a style="left:468px">Support</a>
    <div class="abs search">Search<svg width="11" height="11" viewBox="0 0 11 11"><circle cx="6.5" cy="4.5" r="3.5" fill="none" stroke="#888" stroke-width="1.4"/><path d="M4 7L1 10" stroke="#888" stroke-width="1.6"/></svg></div>
  </nav>

  <section class="abs hero">
    <div class="abs hero-photo" role="img" aria-label="Photo of a smiling woman sitting on a rug using a laptop"></div>
    <div class="abs register">
      <h1>Register your Domain</h1>
      <div class="abs domain-input"><i></i>Enter Desire Domain</div>
      <p>The easlest, fastest way to find avallable domain names</p>
      <div class="abs cta">Get Started<svg width="20" height="20" viewBox="0 0 20 20"><circle cx="10" cy="10" r="10" fill="#fff"/><path d="M8 5.5l6 4.5-6 4.5z" fill="#2a9a1c"/></svg></div>
      <a class="abs adv"><svg width="12" height="12" viewBox="0 0 12 12"><circle cx="6" cy="6" r="3.5" fill="none" stroke="#777" stroke-width="2.5" stroke-dasharray="2 1.2"/><circle cx="6" cy="6" r="1.3" fill="#777"/></svg>Advance Search</a>
    </div>
  </section>

  <h2 class="abs dir-title">Domain Directory</h2>
  <table class="abs directory">
    <thead><tr><th style="width:170px">Country / Organization</th><th style="width:96px">Extension</th><th style="width:186px">Price per year (incl. VAT)</th><th style="width:173px">Category</th><th>Status</th></tr></thead>
    <tbody>
      <tr><td>Belgium</td><td>.be</td><td>€ 17,96</td><td>Business (72,662)</td><td class="buy">Buy Now</td></tr>
      <tr><td>Netherlands</td><td>.nl</td><td>€ 17,96</td><td>Careers (16,382)</td><td class="buy">Buy Now</td></tr>
      <tr><td>Europe</td><td>.eu</td><td>€ 17,96</td><td>Climates (14,968)</td><td class="buy">Buy Now</td></tr>
      <tr><td>Commercial</td><td>.com</td><td>€ 17,96</td><td>Computers (50,339)</td><td class="buy">Buy Now</td></tr>
      <tr><td>Network</td><td>.net</td><td>€ 17,96</td><td>Continents (60,237)</td><td class="sold">Sold Out</td></tr>
      <tr><td>Organization</td><td>.org</td><td>€ 17,96</td><td>Earth Elements (29,838)</td><td class="buy">Buy Now</td></tr>
      <tr><td>Business</td><td>.biz</td><td>€ 17,96</td><td>Education (31,421)</td><td class="buy">Buy Now</td></tr>
      <tr><td>Information</td><td>.info</td><td>€ 17,96</td><td>Energy &amp; Green (35,135)</td><td class="sold">Sold Out</td></tr>
      <tr><td>Germany</td><td>.de</td><td>€ 17,96</td><td>Financial (21,262)</td><td class="buy">Buy Now</td></tr>
    </tbody>
  </table>

  <div class="abs why"><span style="left:19px">Why Choose TILVERA.com?</span><span style="left:522px">Customers Feedback</span><i></i></div>

  <div class="feature">
    <svg class="abs" style="left:16px;top:842px" width="22" height="22" viewBox="0 0 22 22"><circle cx="11" cy="11" r="9.5" fill="none" stroke="#0b3f86" stroke-width="3"/><circle cx="11" cy="11" r="4" fill="none" stroke="#0b3f86" stroke-width="2"/><path d="M11 1v6M11 15v6M1 11h6M15 11h6" stroke="#0b3f86" stroke-width="3"/></svg>
    <h3 style="left:44px;top:842px;color:var(--navy)">24 / 7 Professional Support</h3>
    <p style="left:44px;top:868px">On sait depuis longtemps que travailler avec du texte lisible et contenant.</p>

    <svg class="abs" style="left:272px;top:842px" width="22" height="22" viewBox="0 0 22 22"><path d="M10 3a9 9 0 1 0 9 9h-9z" fill="#d8271f"/><path d="M12 1v9h9a9 9 0 0 0-9-9z" fill="#d8271f"/></svg>
    <h3 style="left:300px;top:842px;color:var(--red)">100% Network and Uptime</h3>
    <p style="left:301px;top:868px">On sait depuis longtemps que travailler avec du texte lisible et contenant.</p>

    <svg class="abs" style="left:15px;top:920px" width="22" height="22" viewBox="0 0 22 22"><path d="M4 9a8 8 0 0 1 14-3M18 13a8 8 0 0 1-14 3" fill="none" stroke="#d9821a" stroke-width="3"/><path d="M19 2v6h-6zM3 20v-6h6z" fill="#d9821a"/></svg>
    <h3 style="left:43px;top:919px;color:var(--orange)">100% Network and Uptime</h3>
    <p style="left:44px;top:947px">On sait depuis longtemps que travailler avec du texte lisible et contenant.</p>

    <svg class="abs" style="left:271px;top:920px" width="22" height="22" viewBox="0 0 22 22"><circle cx="11" cy="11" r="9" fill="none" stroke="#0f7a36" stroke-width="3"/><path d="M11 5v6h5" fill="none" stroke="#0f7a36" stroke-width="2.5"/></svg>
    <h3 style="left:299px;top:919px;color:var(--green-dark)">24 / 7 Professional Support</h3>
    <p style="left:301px;top:947px">On sait depuis longtemps que travailler avec du texte lisible et contenant.</p>
  </div>

  <blockquote class="abs quote" style="left:538px;top:844px">“Le Lorem Ipsum est simplement du faux texte employé dans la composition et la mise en page avant impression.<b>Marta Delgove</b></blockquote>
  <blockquote class="abs quote" style="left:538px;top:920px">“Le Lorem Ipsum est simplement du faux texte employé dans la composition et la mise en page avant impression.<b>Marta Delgove</b></blockquote>

  <footer class="abs footer">
    <h4 style="left:32px">SiteMap</h4>
    <ul style="left:32px"><li>Our Associates</li><li>Our Location</li><li>Our Services</li><li>Our Qualifications</li><li>Our Articles</li><li>External Page</li></ul>
    <h4 style="left:171px">Quick Links</h4>
    <ul style="left:173px"><li>Our Associates</li><li>Our Location</li><li>Our Services</li><li>Our Qualifications</li><li>Our Articles</li><li>External Page</li></ul>
    <h4 style="left:317px">Contact Details</h4>
    <ul style="left:317px;line-height:14.4px"><li>PO Box 418, KELWIN QLD 4512</li><li style="margin-top:7px">Phone: 1 300 724 916</li><li>Fax: 1 300 724 916</li><li style="margin-top:7px">info@tilvera.com</li><li>Map and Directions</li></ul>
    <h4 style="left:507px">Our Location</h4>
    <div class="abs map" role="img" aria-label="Street map showing the office location"></div>
  </footer>
  <div class="abs bottom">Copyright 2012 Website Name. All Rights Reserved.<span>Privacy Policy | Terms &amp; Condition</span></div>
</div>
</body>
</html>
```